Professioal/Creative Northern Harvest Life Insurance Business Card Needed

I need a a creative and professional business card designed for Northern Harvest Life Insurance. Northern Harvest is a life insurance company that caters to mainly blue collar union workers life police, firefighters, teachers, truck drivers, steelworkers, etc. I would like a business card designed that is very professional. The final design should communicate professionalism and life security.

Must compliment company design and logo.

Here is the company website https://www.nhvlife-example.com/#&panel1-1

Target Market(s)

Blue collar workers

Industry/Entity Type

Business

Contact Information for Business Card

Business card should have company logo and comply with colors. Here is the company website https://www.nhvlife-example.com/#&panel1-1

Requirements
Must have
• Name: Dario Kemplen
• Producer

```html
<!DOCTYPE html>
<html lang="en">
<head>
<meta charset="utf-8">
<title>Northern Harvest Life Insurance – Business Card</title>
<link rel="stylesheet" href="https://fonts.googleapis.com/css2?family=Arimo:wght@400;700&display=swap">
<style>
  :root {
    --stage: #e9eaec;
    --back-blue: #2f6d9c;
    --back-blue-dark: #244f74;
    --back-blue-light: #3a80b4;
    --white: #ffffff;
    --front-white: #fbfbfb;
    --accent-orange: #e8a24a;
    --text-blue: #1f4fa3;
    --mark-brown: #7a3512;
    --mark-brown-light: #b4581f;
  }
  * { box-sizing: border-box; margin: 0; padding: 0; }
  html, body {
    width: 1200px; height: 900px; overflow: hidden;
    background: var(--stage);
    font-family: "Arimo", Arial, sans-serif;
  }
  .stage {
    width: 1200px; height: 900px;
    display: flex; flex-direction: column; align-items: center; justify-content: center;
    gap: 40px;
  }
  .card {
    width: 700px; height: 400px;
    border-radius: 22px;
    position: relative; overflow: hidden;
    box-shadow: 0 6px 18px rgba(0,0,0,0.18);
  }

  /* Back side */
  .card--back {
    background: radial-gradient(circle at 50% 40%, var(--back-blue-light) 0%, var(--back-blue) 45%, var(--back-blue-dark) 100%);
  }
  .back__mark {
    position: absolute; left: 50%; top: 150px; transform: translate(-50%, -50%);
    width: 210px; height: 210px; border-radius: 50%;
    border: 4px solid var(--white);
    display: flex; align-items: center; justify-content: center;
    box-shadow: 0 0 10px rgba(255,255,255,0.5);
  }
  .back__name {
    color: var(--white); font-weight: 700; font-size: 26px;
    text-align: center; line-height: 1.15; letter-spacing: 0.5px;
  }
  .back__web {
    position: absolute; left: 0; right: 0; top: 290px;
    text-align: center; color: var(--white); font-size: 20px;
  }

  /* Front side */
  .card--front { background: linear-gradient(135deg, var(--white) 0%, var(--front-white) 60%, #eeeeee 100%); }
  .front__band {
    position: absolute; left: 0; right: 0; bottom: 0; height: 26px;
    background: var(--accent-orange);
  }
  .front__mark {
    position: absolute; left: 60px; top: 85px;
    width: 200px; height: 200px; border-radius: 50%;
    background: radial-gradient(circle at 40% 30%, var(--mark-brown-light) 0%, var(--mark-brown) 70%);
    box-shadow: 0 0 0 3px var(--white), 0 2px 6px rgba(0,0,0,0.25);
    display: flex; align-items: center; justify-content: center;
  }
  .front__mark-name {
    color: var(--white); font-weight: 700; font-size: 24px;
    text-align: center; line-height: 1.15;
  }
  .front__divider {
    position: absolute; left: 330px; top: 95px; width: 2px; height: 170px;
    background: linear-gradient(to bottom, transparent, var(--accent-orange) 30%, var(--accent-orange) 70%, transparent);
  }
  .holder {
    position: absolute; left: 440px; top: 38px;
  }
  .holder__name { color: var(--accent-orange); font-weight: 700; font-size: 22px; }
  .holder__title { color: var(--text-blue); font-weight: 700; font-size: 13px; margin: 3px 0 0 20px; }
  .contacts {
    position: absolute; left: 360px; top: 140px;
    list-style: none; display: flex; flex-direction: column; gap: 14px;
  }
  .contacts__item { display: flex; align-items: flex-start; gap: 14px; color: var(--text-blue); font-size: 17px; line-height: 1.2; }
  .contacts__icon { width: 22px; height: 22px; flex: none; }
</style>
</head>
<body>
<main class="stage">
  <section class="card card--back" aria-label="Card back">
    <div class="back__mark"><span class="back__name">Northern<br>Harvest</span></div>
    <p class="back__web">www.nhvlife-example.com</p>
  </section>

  <section class="card card--front" aria-label="Card front">
    <div class="front__mark"><span class="front__mark-name">Northern<br>Harvest</span></div>
    <div class="front__divider"></div>

    <div class="holder">
      <p class="holder__name">Dario Kemplen</p>
      <p class="holder__title">Producer</p>
    </div>

    <ul class="contacts">
      <li class="contacts__item">
        <svg class="contacts__icon" viewBox="0 0 24 24"><circle cx="12" cy="12" r="10" fill="none" stroke="var(--accent-orange)" stroke-width="2"/><path d="M8.5 7.5c.6-.6 1.4-.4 1.7.2l.8 1.6c.2.5 0 1-.4 1.3l-.6.4c.6 1.4 1.6 2.4 3 3l.4-.6c.3-.4.8-.6 1.3-.4l1.6.8c.6.3.8 1.1.2 1.7-1 1-2.6 1.2-4.4.2-1.8-1-3.3-2.6-4.1-4.4-.7-1.6-.5-2.9.5-3.8z" fill="var(--accent-orange)"/></svg>
        <span>1-800-555-0192</span>
      </li>
      <li class="contacts__item">
        <svg class="contacts__icon" viewBox="0 0 24 24"><rect x="2" y="5" width="20" height="14" fill="none" stroke="var(--accent-orange)" stroke-width="2"/><path d="M2 5l10 8 10-8" fill="none" stroke="var(--accent-orange)" stroke-width="2"/></svg>
        <span>name@nhvlife-example.com</span>
      </li>
      <li class="contacts__item">
        <svg class="contacts__icon" viewBox="0 0 24 24"><circle cx="12" cy="12" r="10" fill="var(--accent-orange)"/><path d="M2 12h20M12 2c3 3 3 17 0 20M12 2c-3 3-3 17 0 20M4 7h16M4 17h16" fill="none" stroke="var(--white)" stroke-width="1.4"/></svg>
        <span>www.nhvlife-example.com</span>
      </li>
      <li class="contacts__item">
        <svg class="contacts__icon" viewBox="0 0 24 24"><path d="M12 2a7 7 0 0 0-7 7c0 5 7 13 7 13s7-8 7-13a7 7 0 0 0-7-7z" fill="var(--accent-orange)"/><circle cx="12" cy="9" r="2.5" fill="var(--white)"/></svg>
        <span>450 Cedar Ridge Ln,<br>Fairview, TX 75000, United States</span>
      </li>
    </ul>

    <div class="front__band"></div>
  </section>
</main>
</body>
</html>
```